Power Point for new apartment development

I need to create a power point that will help me present a new real estate development. I have put together the powerpoint without any graphics...just the highlights and included a bunch of pics attached to this post. Use them as needed when discussing each slide. I'm really looking to nail this. dont have much time so please work quick and i'll accept the second i like one.
Target Market(s)
investors and financing institutions
Industry/Entity Type
Real Estate
Font styles to use
Serif
Requirements
Must have
- just needs to be awesome... all your choice.
Nice to have
- nothing specific
Should not have
- nothing specific

```html
<!DOCTYPE html>
<html lang="en">
<head>
<meta charset="utf-8">
<title>Brightnest Residences – Presentation Deck</title>
<link rel="stylesheet" href="https://fonts.googleapis.com/css2?family=Oswald:wght@400;500&family=Roboto+Condensed:wght@400;700&family=Lora:ital@1&display=swap">
<style>
:root{
  --lime:#c3c91c;
  --blue:#2c5ea9;
  --blue-deep:#23508f;
  --ink:#333;
  --grey:#6f6f6f;
  --paper:#f5f5f5;
  --dark:#3b3b3d;
  --stage:#141414;
}
*{box-sizing:border-box;margin:0;padding:0}
html,body{width:1200px;height:1200px;overflow:hidden;background:var(--stage)}
.deck{position:relative;width:1200px;height:1200px;display:grid;
  grid-template-columns:repeat(3,380px);grid-template-rows:repeat(4,286px);
  column-gap:9px;row-gap:8px;padding:10px 17px 0 17px}
.slide{position:relative;overflow:hidden;background:var(--paper);
  font-family:"Roboto Condensed",sans-serif;color:var(--ink)}
.abs{position:absolute}
.brand{position:absolute;top:10px;right:10px;display:flex;align-items:center;gap:4px;
  font-family:"Oswald",sans-serif;font-weight:500;font-size:15px;color:var(--lime);letter-spacing:.3px}
.brand i{display:block;width:9px;height:9px;border-radius:50%;background:var(--blue)}
.foot{position:absolute;left:0;right:0;bottom:0;height:7px;background:var(--blue)}
.heading{position:absolute;top:24px;font-family:"Oswald",sans-serif;font-weight:400;font-size:12px;
  letter-spacing:.4px;color:#222;text-align:center;padding:0 6px 2px;border-bottom:2px solid var(--blue)}
.heading b{font-weight:500}
.body{font-size:6px;line-height:1.6;color:#444}
.italic{font-family:"Lora",serif;font-style:italic;color:var(--blue);font-size:7.4px;line-height:1.55}
.photo{position:absolute}
.title-condensed{font-family:"Oswald",sans-serif;font-weight:400;color:var(--blue);font-size:17px;letter-spacing:-.2px;line-height:1}
.subtitle{font-family:"Oswald",sans-serif;font-size:7px;color:#555;letter-spacing:.2px}
.list{list-style:none;font-size:6.6px;color:#fff}
.list li{position:relative;padding-left:14px;margin-bottom:5.6px;line-height:1.25}
.list li::before{content:"";position:absolute;left:0;top:0;width:6px;height:6px;border-radius:50%;border:1.5px solid var(--lime)}
.circle{position:absolute;border-radius:50%;border:3px solid #fff;box-shadow:0 1px 3px rgba(0,0,0,.35)}
.card{position:absolute;top:98px;width:118px;height:164px;background:#fff;border-radius:5px;box-shadow:0 1px 4px rgba(0,0,0,.25);overflow:hidden}
.card h4,.colhead{font-family:"Oswald",sans-serif;font-weight:400;font-size:9.5px;color:#fff;text-align:center;line-height:30px;height:30px}
.yellow{color:var(--lime)}
</style>
</head>
<body>
<main class="deck">

<!-- 1 cover -->
<section class="slide cover" style="background:linear-gradient(180deg,#4a4f58 0%,#3c4149 55%,#2d3036 100%)">
  <div class="photo" role="img" aria-label="City skyline with high-rise towers by the river at dusk" style="inset:0;background:linear-gradient(180deg,#575d67 0%,#454a52 45%,#34373c 100%)"></div>
  <div class="abs" style="left:0;right:0;top:165px;height:52px;background:rgba(30,30,32,.55)"></div>
  <div class="abs" style="left:0;right:0;top:122px;text-align:center;font-family:'Oswald',sans-serif;font-size:18px;color:#fff">Project Title Here</div>
  <div class="abs" style="left:112px;top:172px;display:flex;align-items:center;gap:8px;font-family:'Oswald',sans-serif;font-weight:500;font-size:32px;color:var(--lime)">Brightnest<span style="display:block;width:20px;height:20px;border-radius:50%;background:var(--blue)"></span></div>
</section>

<!-- 2 company overview -->
<section class="slide">
  <div class="brand">Brightnest<i></i></div>
  <div class="heading" style="left:130px">COMPANY <b>OVERVIEW</b></div>
  <div class="circle" style="left:16px;top:92px;width:68px;height:68px;background:var(--blue)"><div style="color:#fff;font-size:5px;text-align:center;padding:10px 8px 0;line-height:1.4"><b class="yellow" style="font-size:6.5px">Title Here</b><br>Lorem ipsum is simply dummy text of the printing industry</div></div>
  <div class="circle" role="img" aria-label="Tanning bed" style="left:88px;top:98px;width:50px;height:50px;background:linear-gradient(135deg,#e8eef2,#b9c7cf)"></div>
  <div class="abs" style="left:131px;top:82px;width:34px;height:34px;border-radius:50%;background:#d9df2a;text-align:center;font-family:'Oswald',sans-serif;font-size:12px;line-height:1;padding-top:6px">9<br><span style="font-size:6px">Minute</span></div>
  <div class="abs" style="left:65px;top:83px;width:20px;height:20px;border-radius:50%;background:#333"></div>
  <div class="abs" style="left:170px;top:118px;width:20px;height:20px;border-radius:50%;background:#333"></div>
  <div class="circle" style="left:132px;top:122px;width:60px;height:60px;background:#333"><div style="color:#fff;font-size:4.8px;text-align:center;padding:9px 6px 0;line-height:1.4"><b class="yellow" style="font-size:6.5px">Title Here</b><br>Lorem ipsum is simply dummy text of the printing</div></div>
  <div class="circle" role="img" aria-label="Group of residents" style="left:16px;top:172px;width:48px;height:48px;background:linear-gradient(135deg,#dfe6ee,#9fb5cc)"></div>
  <div class="circle" role="img" aria-label="Row of treadmills" style="left:68px;top:158px;width:42px;height:42px;background:linear-gradient(135deg,#7b8592,#3e4550)"></div>
  <div class="circle" role="img" aria-label="Cardio machines" style="left:108px;top:182px;width:42px;height:42px;background:linear-gradient(135deg,#c9c1b4,#6d6357)"></div>
  <div class="abs" style="left:223px;top:80px;width:148px">
    <div style="font-size:7.5px;margin-bottom:5px">Subtext here</div>
    <p class="body">Lorem Ipsum is simply dummy text of the printing and typesetting industry. Lorem Ipsum has been the industry's standard dummy text ever since the 1500s, when an unknown printer took a galley of type and scrambled it to make a type specimen book. It has survived not only five centuries, but also the leap into electronic typesetting.</p>
    <p class="body" style="margin-top:4px">Lorem Ipsum is simply dummy text of the printing and typesetting industry. Lorem Ipsum has been the industry's standard dummy text ever since the 1500s, when an unknown printer took a galley of type and scrambled it to make a type specimen book. It has survived not only five centuries, but also the leap into electronic typesetting.</p>
  </div>
  <div class="foot"></div>
</section>

<!-- 3 our feature -->
<section class="slide">
  <div class="brand">Brightnest<i></i></div>
  <div class="heading" style="left:150px">OUR FEATURE</div>
  <p class="italic abs" style="left:17px;top:66px;width:170px">Lorem Ipsum is simply dummy text of the printing and typesetting industry. Lorem Ipsum has been the industry's standard dummy text Lorem Ipsum is simply dummy text of the printing and typesetting industry. Lorem Ipsum has been the industry's standard dummy text</p>
  <p class="body abs" style="left:17px;top:145px;width:172px;text-align:justify">Lorem Ipsum is simply dummy text of the printing and typesetting industry. Lorem Ipsum has been the industry's standard dummy text. Lorem Ipsum is simply dummy text of the printing and typesetting industry.</p>
  <p class="body abs" style="left:17px;top:192px;width:172px;text-align:justify">Lorem Ipsum has been the industry's standard dummy text Lorem Ipsum is simply dummy text of the printing and typesetting industry. Lorem Ipsum has been the industry's standard dummy text. Lorem Ipsum is simply dummy text of the printing and typesetting industry.</p>
  <div class="photo" role="img" aria-label="Riverside tower and city buildings under a blue sky" style="left:203px;top:58px;width:177px;height:200px;background:linear-gradient(180deg,#cfdcea 0%,#9fb4c9 45%,#6c7b86 70%,#56656f 100%)"></div>
  <div class="foot"></div>
</section>

<!-- 4 project portfolio -->
<section class="slide">
  <div class="brand">Brightnest<i></i></div>
  <div class="abs" style="left:11px;top:10px"><div class="title-condensed">PROJECT PORTFOLIO</div><div class="subtitle" style="margin-top:3px">SUBTEXT HERE SUBTEXT HERE SUBTEXT HERE SUBTEXT HERE</div></div>
  <p class="abs" style="left:9px;top:60px;width:362px;font-size:5.8px;line-height:1.55;color:var(--blue)">Lorem Ipsum is simply dummy text of the printing and typesetting industry. Lorem Ipsum has been the industry's standard dummy text ever since the 1500s, Lorem Ipsum is simply dummy text of the printing and typesetting industry. Lorem Ipsum has been the industry's standard dummy text ever since the 1500s,</p>
  <div class="card" style="left:7px"><h4 style="background:var(--lime)">SUB TITLE TEXT HERE</h4><div role="img" aria-label="Tanning bed" style="margin:24px 6px 0;height:86px;background:linear-gradient(135deg,#f0f3f6,#bfc9d2);border-radius:6px"></div></div>
  <div class="card" style="left:131px"><h4 style="background:var(--blue)">SUB TITLE TEXT HERE</h4><div role="img" aria-label="Valet key fob with wireless signal" style="margin:14px 30px 0;height:110px;background:linear-gradient(180deg,#5bb7d3 0%,#3a3a3a 30%,#2d2d2d 100%);border-radius:8px"></div></div>
  <div class="card" style="left:255px"><h4 style="background:#a8a8a8">SUB TITLE TEXT HERE</h4><div role="img" aria-label="Person training on a functional fitness rig" style="margin:10px 4px 0;height:116px;background:linear-gradient(180deg,#f3f3f3,#cfcfcf)"></div></div>
  <div class="abs" style="left:0;right:0;bottom:0;height:9px;background:var(--lime)"></div>
</section>

<!-- 5 property amenities -->
<section class="slide" style="background:var(--blue)">
  <div class="photo" role="img" aria-label="Bright penthouse lounge with floor-to-ceiling windows overlooking the water" style="left:178px;top:0;right:0;bottom:0;background:linear-gradient(180deg,#e9eef2 0%,#cbd9e3 45%,#9ab7cc 60%,#e6e6e6 75%,#cfcfcf 100%)"></div>
  <div class="brand">Brightnest<i></i></div>
  <div class="abs" style="left:10px;top:9px;font-family:'Oswald',sans-serif;color:#fff;font-size:12.5px;padding-bottom:3px;border-bottom:2px solid var(--lime);width:140px">PROPERTY AMENITIES</div>
  <ul class="list abs" style="left:10px;top:35px;width:165px">
    <li>24 Hour Valet Services</li><li>State Of The Art Health &amp; Fitness Facility</li><li>Office Suites For Lease</li><li>Micro Convenience Store On Site</li><li>Entire Building is "Smart" operated and managed</li><li>Tenant Office &amp; Conference Room including; Computer, wifi, Print, Fax, Scan, Copy Center</li><li>Outdoor lounges &amp; fireplaces</li><li>Luxury Clubhouse With 73" Smart TV, Patio With Custom Built Outdoor Pizza Oven and Grill, as well as Jacuzzi</li><li>Rooftop Landscaped Dog Park and Private Sanctuary Full of Plants and Flowers.</li><li>Wine cellar*</li><li>ILounge</li><li>Dog Park</li><li>Dog wash bay</li>
  </ul>
</section>

<!-- 6 project title -->
<section class="slide">
  <div class="brand">Brightnest<i></i></div>
  <div class="abs" style="left:11px;top:10px"><div class="title-condensed">PROJECT TITLE HERE</div><div class="subtitle" style="margin-top:3px">SUBTEXT HERE SUBTEXT HERE SUBTEXT HERE SUBTEXT HERE</div></div>
  <div class="abs" style="left:0;right:0;top:54px;display:grid;grid-template-columns:repeat(3,1fr)">
    <div class="colhead" style="background:var(--lime)">SUB TITLE TEXT HERE</div>
    <div class="colhead" style="background:var(--blue)">SUB TITLE TEXT HERE</div>
    <div class="colhead" style="background:var(--dark)">SUB TITLE TEXT HERE</div>
  </div>
  <div class="photo" role="img" aria-label="Apartment tower facade" style="left:0;top:84px;width:127px;bottom:0;background:linear-gradient(180deg,#c9d4de,#7e8894)"></div>
  <div class="photo" role="img" aria-label="Building with balconies" style="left:127px;top:84px;width:127px;bottom:0;background:linear-gradient(180deg,#d9cdb9,#8d7f6b)"></div>
  <div class="photo" role="img" aria-label="Convenience store shelves" style="left:254px;top:84px;right:0;bottom:0;background:linear-gradient(180deg,#b08b64,#7a5a3f)"></div>
  <div class="abs" style="left:0;right:0;top:226px;height:60px;background:rgba(50,50,52,.82);color:#ddd;font-size:5.8px;line-height:1.9;text-align:center;padding:7px 10px">Lorem Ipsum is simply dummy text of the printing and typesetting industry. Lorem Ipsum has been the industry's standard dummy text ever since the 1500s, Lorem Ipsum is simply dummy text of the printing and typesetting industry. Lorem Ipsum has been the industry's standard dummy text.</div>
</section>

<!-- 7 residence features -->
<section class="slide">
  <div class="photo" role="img" aria-label="Modern apartment building exterior with street cafe" style="inset:0;background:linear-gradient(90deg,#8f8f8a,#c6b59c 70%,#a58e6e)"></div>
  <div class="abs" style="left:51px;top:0;width:204px;bottom:0;background:rgba(44,94,169,.88)"></div>
  <div class="brand">Brightnest<i></i></div>
  <div class="abs" style="left:63px;top:9px;font-family:'Oswald',sans-serif;color:#fff;font-size:12.5px;padding-bottom:3px;border-bottom:2px solid var(--lime);width:170px">RESIDENCE FEATURES</div>
  <ul class="list abs" style="left:63px;top:36px;width:180px">
    <li>Floor to ceiling windows facing Cedar River</li><li>Extremely Usable balconies which convert to four season rooms during winter</li><li>Elevator opens inside each apartment unit providing direct access</li><li>Quartz stone countertops</li><li>Custom tile in kitchen and bathrooms*</li><li>Alderline kitchen &amp; bathroom fixtures</li><li>Stainless steel and "smart appliances"</li><li>Heated flooring throughout entire apartment</li><li>"Real" Hardwood Flooring</li><li>Walk-in and Coastline Closets</li><li>USB outlets for charging</li><li>Prewired media outlets</li><li>Full-size stackable washer/dryer</li>
  </ul>
</section>

<!-- 8 smart health -->
<section class="slide" style="background:var(--blue-deep)">
  <div class="brand">Brightnest<i></i></div>
  <div class="abs" style="left:7px;top:9px;font-family:'Oswald',sans-serif;color:#fff;font-size:11.5px">SMART HEALTH &amp; FITNESS FACILITY</div>
  <div class="abs" style="left:0;right:0;top:25px;height:1px;background:rgba(255,255,255,.35)"></div>
  <div class="abs" style="left:18px;top:38px;width:350px;color:#fff">
    <div class="yellow" style="font-size:7.5px;margin-bottom:4px">Subtext here</div>
    <p style="font-size:5.9px;line-height:1.75">Lorem Ipsum is simply dummy text of the printing and typesetting industry. Lorem Ipsum has been the industry's standard dummy text ever since the 1500s, when an unknown printer took a galley of type and scrambled it to make a type specimen book. It has survived not only five centuries, but also the leap into electronic typesetting.</p>
    <div class="yellow" style="font-size:7.5px;margin:10px 0 4px">Subtext here</div>
    <p style="font-size:5.9px;line-height:1.75">Lorem Ipsum is simply dummy text of the printing and typesetting industry. Lorem Ipsum has been the industry's standard dummy text ever since the 1500s, when an unknown printer took a galley of type and scrambled it to make a type specimen book. It has survived not only five centuries, but also the leap into electronic typesetting.</p>
  </div>
  <div class="abs" style="left:0;right:0;top:198px;bottom:0;background:var(--lime)"></div>
  <div class="circle" role="img" aria-label="Treadmills" style="left:5px;top:169px;width:66px;height:66px;background:linear-gradient(135deg,#c8d2dc,#6d7884)"></div>
  <div class="circle" role="img" aria-label="Row of exercise bikes" style="left:81px;top:169px;width:66px;height:66px;background:linear-gradient(135deg,#8c96a2,#3b424c)"></div>
  <div class="circle" role="img" aria-label="Resident lifting weights" style="left:157px;top:169px;width:66px;height:66px;background:linear-gradient(135deg,#e3dfd5,#9b8f7d)"></div>
  <div class="circle" role="img" aria-label="Group of happy residents" style="left:233px;top:169px;width:66px;height:66px;background:linear-gradient(135deg,#e5ecf3,#9fb5cc)"></div>
  <div class="circle" role="img" aria-label="Person training with dumbbells" style="left:309px;top:169px;width:66px;height:66px;background:linear-gradient(135deg,#6f5b48,#2e2620)"></div>
  <p class="abs" style="left:18px;top:243px;width:350px;font-size:5.9px;line-height:1.75;color:#333">Lorem Ipsum is simply dummy text of the printing and typesetting industry. Lorem Ipsum has been the industry's standard dummy text ever since the 1500s, when an unknown printer took a galley of type and scrambled it to make a type specimen book. It has survived not only five centuries, but also the leap into electronic typesetting.</p>
</section>

<!-- 9 our feature -->
<section class="slide">
  <div class="brand">Brightnest<i></i></div>
  <div class="heading" style="left:145px">OUR FEATURE</div>
  <p class="italic abs" style="left:12px;top:64px;width:170px">Lorem Ipsum is simply dummy text of the printing and typesetting industry. Lorem Ipsum has been the industry's standard dummy text Lorem Ipsum is simply dummy text of the printing and typesetting industry. Lorem Ipsum has been the industry's standard dummy text</p>
  <p class="body abs" style="left:12px;top:144px;width:172px;text-align:justify">Lorem Ipsum is simply dummy text of the printing and typesetting industry. Lorem Ipsum has been the industry's standard dummy text. Lorem Ipsum is simply dummy text of the printing and typesetting industry.</p>
  <p class="body abs" style="left:12px;top:194px;width:172px;text-align:justify">Lorem Ipsum has been the industry's standard dummy text Lorem Ipsum is simply dummy text of the printing and typesetting industry. Lorem Ipsum has been the industry's standard dummy text. Lorem Ipsum is simply dummy text of the printing and typesetting industry. Lorem Ipsum has been the industry's standard dummy text</p>
  <div class="photo" role="img" aria-label="Athletes training on a functional fitness rig" style="left:195px;top:75px;width:180px;height:190px;background:radial-gradient(ellipse at 55% 55%,#d4d4d4 0%,#f5f5f5 70%)"></div>
  <div class="foot"></div>
</section>

<!-- 10 our team -->
<section class="slide">
  <div class="brand">Brightnest<i></i></div>
  <div class="heading" style="left:127px;top:28px;padding:0 38px 2px">OUR TEAM</div>
  <div class="abs" style="left:0;right:0;top:90px;display:grid;grid-template-columns:repeat(3,1fr);text-align:center">
    <div><div role="img" aria-label="Team member portrait" style="margin:0 auto;width:64px;height:64px;border-radius:50%;border:3px solid #fff;box-shadow:0 0 0 1px #bbb;background:linear-gradient(180deg,#cfcfcf,#8d8d8d)"></div><div style="color:var(--blue);font-size:8.5px;font-weight:700;margin:12px 0 4px">Subtext here</div><p class="body" style="padding:0 14px">Lorem Ipsum is simply dummy text of the printing and typesetting industry. Lorem Ipsum has been the industry's standard dummy text</p></div>
    <div><div role="img" aria-label="Team member portrait" style="margin:0 auto;width:64px;height:64px;border-radius:50%;border:3px solid #fff;box-shadow:0 0 0 1px #bbb;background:linear-gradient(180deg,#cfcfcf,#8d8d8d)"></div><div style="color:var(--blue);font-size:8.5px;font-weight:700;margin:12px 0 4px">Subtext here</div><p class="body" style="padding:0 14px">Lorem Ipsum is simply dummy text of the printing and typesetting industry. Lorem Ipsum has been the industry's standard dummy text</p></div>
    <div><div role="img" aria-label="Team member portrait" style="margin:0 auto;width:64px;height:64px;border-radius:50%;border:3px solid #fff;box-shadow:0 0 0 1px #bbb;background:linear-gradient(180deg,#cfcfcf,#8d8d8d)"></div><div style="color:var(--blue);font-size:8.5px;font-weight:700;margin:12px 0 4px">Subtext here</div><p class="body" style="padding:0 14px">Lorem Ipsum is simply dummy text of the printing and typesetting industry. Lorem Ipsum has been the industry's standard dummy text</p></div>
  </div>
  <div class="foot"></div>
</section>

<!-- 11 our feature with screen -->
<section class="slide">
  <div class="brand">Brightnest<i></i></div>
  <div class="heading" style="left:135px;top:28px;padding:0 20px 2px">OUR FEATURE</div>
  <p class="italic abs" style="left:10px;top:60px;width:360px;text-align:center;font-size:8px">Lorem Ipsum is simply dummy text of the printing and typesetting industry. Lorem Ipsum has been the industry's standard dummy text Lorem Ipsum is simply dummy text of the printing and typesetting industry.<br>Lorem Ipsum has been the industry's standard dummy text</p>
  <svg class="abs" style="left:0;top:0" width="380" height="286" aria-hidden="true">
    <g stroke="#777" stroke-width=".6"><line x1="62" y1="142" x2="112" y2="142"/><line x1="62" y1="198" x2="112" y2="198"/><line x1="260" y1="144" x2="318" y2="144"/><line x1="260" y1="201" x2="318" y2="201"/></g>
    <rect x="112" y="130" width="148" height="98" rx="4" fill="#2a2a2a"/>
    <rect x="165" y="228" width="42" height="12" fill="#cfcfcf"/><rect x="150" y="240" width="72" height="4" rx="2" fill="#bdbdbd"/>
  </svg>
  <div class="photo" role="img" aria-label="Convenience store interior on a monitor" style="left:117px;top:135px;width:138px;height:85px;background:linear-gradient(180deg,#c4a07a,#8a6646)"></div>
  <div class="abs body" style="left:12px;top:136px;width:100px;font-size:5px"><b style="color:var(--blue);font-size:6px;font-weight:400">Subtext Title here</b><br><span style="display:block;margin-top:3px">Lorem Ipsum is simply dummy text of the printing and typesetting industry. Lorem Ipsum has been the industry's standard dummy text</span></div>
  <div class="abs body" style="left:12px;top:192px;width:100px;font-size:5px"><b style="color:var(--blue);font-size:6px;font-weight:400">Subtext Title here</b><br><span style="display:block;margin-top:3px">Lorem Ipsum is simply dummy text of the printing and typesetting industry. Lorem Ipsum has been the industry's standard dummy text</span></div>
  <div class="abs body" style="left:280px;top:138px;width:95px;font-size:5px"><b style="color:var(--blue);font-size:6px;font-weight:400">Subtext Title here</b><br><span style="display:block;margin-top:3px">Lorem Ipsum is simply dummy text of the printing and typesetting industry. Lorem Ipsum has been the industry's standard dummy text</span></div>
  <div class="abs body" style="left:280px;top:195px;width:95px;font-size:5px"><b style="color:var(--blue);font-size:6px;font-weight:400">Subtext Title here</b><br><span style="display:block;margin-top:3px">Lorem Ipsum is simply dummy text of the printing and typesetting industry. Lorem Ipsum has been the industry's standard dummy text</span></div>
  <div class="foot"></div>
</section>

<!-- 12 feature icons -->
<section class="slide">
  <div class="brand">Brightnest<i></i></div>
  <div class="heading" style="left:150px;top:10px">OUR FEATURE</div>
  <div class="abs" style="left:20px;right:14px;top:40px;display:grid;grid-template-columns:repeat(4,1fr);row-gap:14px;text-align:center">
    <div><div role="img" aria-label="Bathtub icon" style="margin:0 auto;width:36px;height:36px;border-radius:6px;background:linear-gradient(135deg,#dfe9f2,#9fb8cf)"></div><div style="color:var(--blue);font-size:6px;margin-top:6px">Subtext Title here</div><div style="font-size:5px">Lorem Ipsum is simply dummy</div></div>
    <div><div role="img" aria-label="House icon" style="margin:0 auto;width:36px;height:36px;border-radius:6px;background:linear-gradient(135deg,#f3c26a,#7fa3c8)"></div><div style="color:var(--blue);font-size:6px;margin-top:6px">Subtext Title here</div><div style="font-size:5px">Lorem Ipsum is simply dummy</div></div>
    <div><div role="img" aria-label="Heated radiator icon" style="margin:0 auto;width:36px;height:36px;border-radius:6px;background:linear-gradient(135deg,#e4e4e4,#b3b3b3)"></div><div style="color:var(--blue);font-size:6px;margin-top:6px">Subtext Title here</div><div style="font-size:5px">Lorem Ipsum is simply dummy</div></div>
    <div><div role="img" aria-label="Garage icon" style="margin:0 auto;width:36px;height:36px;border-radius:6px;background:linear-gradient(135deg,#f2b45a,#d9d9d9)"></div><div style="color:var(--blue);font-size:6px;margin-top:6px">Subtext Title here</div><div style="font-size:5px">Lorem Ipsum is simply dummy</div></div>
    <div><div role="img" aria-label="Exercise bike icon" style="margin:0 auto;width:36px;height:36px;border-radius:6px;background:linear-gradient(135deg,#d9d9d9,#7d7d7d)"></div><div style="color:var(--blue);font-size:6px;margin-top:6px">Subtext Title here</div><div style="font-size:5px">Lorem Ipsum is simply dummy</div></div>
    <div><div role="img" aria-label="Floor plan with magnifier icon" style="margin:0 auto;width:36px;height:36px;border-radius:6px;background:linear-gradient(135deg,#f4e4b8,#9fc18d)"></div><div style="color:var(--blue);font-size:6px;margin-top:6px">Subtext Title here</div><div style="font-size:5px">Lorem Ipsum is simply dummy</div></div>
    <div><div role="img" aria-label="Swimming pool icon" style="margin:0 auto;width:36px;height:36px;border-radius:6px;background:linear-gradient(135deg,#d5ecf7,#6fb2d9)"></div><div style="color:var(--blue);font-size:6px;margin-top:6px">Subtext Title here</div><div style="font-size:5px">Lorem Ipsum is simply dummy</div></div>
    <div><svg width="36" height="36" viewBox="0 0 36 36" aria-label="Wi-Fi icon" role="img"><g fill="none" stroke="#2a8fd6" stroke-width="3" stroke-linecap="round"><path d="M6 15a17 17 0 0 1 24 0"/><path d="M11 20a10 10 0 0 1 14 0"/></g><circle cx="18" cy="26" r="2.6" fill="#2a8fd6"/></svg><div style="color:var(--blue);font-size:6px;margin-top:6px">Subtext Title here</div><div style="font-size:5px">Lorem Ipsum is simply dummy</div></div>
    <div><div role="img" aria-label="Fireplace icon" style="margin:0 auto;width:36px;height:36px;border-radius:6px;background:linear-gradient(135deg,#d9d9d9,#e87a2e)"></div><div style="color:var(--blue);font-size:6px;margin-top:6px">Subtext Title here</div><div style="font-size:5px">Lorem Ipsum is simply dummy</div></div>
    <div><div role="img" aria-label="Keys icon" style="margin:0 auto;width:36px;height:36px;border-radius:6px;background:linear-gradient(135deg,#eeeeee,#a9a9a9)"></div><div style="color:var(--blue);font-size:6px;margin-top:6px">Subtext Title here</div><div style="font-size:5px">Lorem Ipsum is simply dummy</div></div>
    <div><div role="img" aria-label="Hardwood flooring icon" style="margin:0 auto;width:36px;height:36px;border-radius:6px;background:linear-gradient(135deg,#f6d27a,#e39a3a)"></div><div style="color:var(--blue);font-size:6px;margin-top:6px">Subtext Title here</div><div style="font-size:5px">Lorem Ipsum is simply dummy</div></div>
    <div><div role="img" aria-label="Smart TV icon" style="margin:0 auto;width:36px;height:36px;border-radius:6px;background:linear-gradient(135deg,#4fb7e6,#2c2c2c)"></div><div style="color:var(--blue);font-size:6px;margin-top:6px">Subtext Title here</div><div style="font-size:5px">Lorem Ipsum is simply dummy</div></div>
  </div>
  <div class="foot"></div>
</section>

</main>
</body>
</html>
```